Simple Modern Label for a Coconut oil product

We need a label designed for Organic Coconut oil. We would like the label to convey the gourmet/high quality product. It should be modern and simple and look like an artisinal product. The label will need to contain all the basic label requirements - Independence list, place for nutrition facts, our company logo etc.
The label will ultimately be printed as oil proof, so it will have a glossy appearance.
I have includes some examples that I like and a file with the logo.

Product Container - Wide Mount Clear Glass Jar: 4.75 inches tall (base to the bottom of the lid) and 9.5 in circumference
Label: Can be 1 or 2 separate labels, round, square and rectangle are okay
No larger than 3 inches high and 9 inches long

Target Market(s)

Middle Age home chef

Industry/Entity Type

Product

Requirements
Must have
• - logo (Attached below, I have this in multiple formats, let me know if you need them)
• - 14 FL OZ (414mL)
• - ingredient: organic unrefined whole kernel virgin coconut oil,
• - Manufacturer: XXX Y St., anywhere, CA, 99999
• - Distributed by Meadowfern Naturals, P.O. Box 5521, Oakland, CA 94612 www.MeadowfernNaturals.example
• - Certified Organic by Company Name
• - Product of Sri Lanka
Nice to have
• - Nutrition Facts
Should not have
• Clutter

```html
<!DOCTYPE html>
<html lang="en">
<head>
<meta charset="utf-8">
<title>Meadowfern Naturals – Organic Unrefined Coconut Oil Label</title>
<link rel="stylesheet" href="https://fonts.googleapis.com/css2?family=Josefin+Sans:wght@300;600;700&display=swap">
<style>
  :root {
    --canvas: #ffffff;
    --paper: #f6f2dc;
    --frond-dark: #2f6b1c;
    --frond-mid: #4f8f2a;
    --frond-light: #8dbb5a;
    --band-orange: #f5821f;
    --ink-white: #ffffff;
  }
  html, body {
    margin: 0;
    padding: 0;
    width: 1200px;
    height: 1200px;
    overflow: hidden;
    background: var(--canvas);
  }
  .canvas {
    position: relative;
    width: 1200px;
    height: 1200px;
    background: var(--canvas);
  }
  .label {
    position: absolute;
    left: 100px;
    top: 153px;
    width: 1000px;
    height: 894px;
    background: var(--paper);
    overflow: hidden;
  }
  .label-artwork {
    position: absolute;
    inset: 0;
    background:
      radial-gradient(ellipse 55% 50% at 50% 22%, var(--frond-mid) 0%, var(--frond-dark) 45%, rgba(47,107,28,0) 75%),
      radial-gradient(ellipse 45% 40% at 85% 70%, var(--frond-mid) 0%, rgba(79,143,42,0) 70%),
      radial-gradient(ellipse 40% 35% at 45% 92%, var(--frond-dark) 0%, rgba(47,107,28,0) 70%),
      radial-gradient(ellipse 30% 30% at 10% 30%, var(--frond-light) 0%, rgba(141,187,90,0) 70%),
      var(--paper);
  }
  .title-band {
    position: absolute;
    left: 0;
    top: 365px;
    width: 741px;
    height: 333px;
    background: var(--band-orange);
    color: var(--ink-white);
    font-family: "Josefin Sans", sans-serif;
  }
  .brand-block {
    position: absolute;
    left: 20px;
    top: 0;
    width: 208px;
    height: 100%;
  }
  .brand-name {
    position: absolute;
    left: 0;
    right: 0;
    top: 92px;
    text-align: center;
    font-weight: 700;
    font-size: 27px;
    line-height: 1.15;
    letter-spacing: 0.5px;
    text-transform: uppercase;
  }
  .net-contents {
    position: absolute;
    right: 0;
    top: 232px;
    text-align: right;
    font-weight: 600;
    font-size: 16px;
    line-height: 1.45;
    letter-spacing: 0.5px;
  }
  .divider {
    position: absolute;
    left: 256px;
    top: 34px;
    width: 3px;
    height: 268px;
    background: var(--ink-white);
  }
  .product-name {
    position: absolute;
    left: 287px;
    top: 42px;
    margin: 0;
    font-size: 62px;
    line-height: 67px;
    letter-spacing: 2px;
    text-transform: uppercase;
  }
  .product-name .descriptor { display: block; font-weight: 300; }
  .product-name .product { display: block; font-weight: 700; }
</style>
</head>
<body>
  <main class="canvas">
    <section class="label">
      <div class="label-artwork" role="img" aria-label="Botanical illustration of a coconut palm crown with green fronds and coconuts on a cream paper background"></div>
      <div class="title-band">
        <div class="brand-block">
          <div class="brand-name">Meadowfern<br>Naturals</div>
          <div class="net-contents">14 FL OZ<br>—<br>414 ML</div>
        </div>
        <div class="divider"></div>
        <h1 class="product-name">
          <span class="descriptor">Organic</span>
          <span class="descriptor">Unrefined</span>
          <span class="product">Coconut</span>
          <span class="product">Oil</span>
        </h1>
      </div>
    </section>
  </main>
</body>
</html>
```